Flyer for an pediatric sleep consultancy - to distribute to play and childcare centers etc.

I need a flyer that will attract the attention of parents with children between the age of babies to toddlers, who may be experiencing sleep issues. The flyer will be placed at places such as community centers, doctors room, play centers, kindergardens, etc.

My company is called "The Quiet Meadow Studio" and provides a sleep consultancy service. My service essentially provides a customized plan for parents to follow and general advice and guidance. It is not medical advice.

I like to the flyer to have an overall tone that is soft and peaceful with a clean and beautiful design, however can catch the attention of parents who may be struggling with their child's sleep issues and are sleep deprived. I would like photos with minimal text. The colour I use is a brownish rose. I will attach some of my designs to give you an idea. You can have a look at my homepage as well to get an idea about my esthetic direction and the colour. Although the colour of my page is a bit too brownish....

I will provide the text to appear in the flyer once I have a better idea of the layout that I prefer for the flyer. The text however wont be extensive, just some catchy points.

I want to direct people to my website which is www.quietmeadowstudio-example.com
I offer a first FREE evaluation call, to the parents, to get to know each other better, learn about their child's particular sleep problems and see if we are a good fit and can work together. I would like to have this information somehow on the flyer, so that the parents will contact me.
I also have a facebook page, which is: The Quiet Meadow Studio

I have a logo that I would like to appear on the flyer. I will attach the file once the uploader on art bazaar is fixed.

When I print the flyer - I like to print A5 SIZE ... please make sure the formatting is OK for this size.

Here are some text ideas. of course all of it would be too much, I guess. On the front of the flyer I would like to have some catchy phrase or something similar to get people interested and to want to know more. On the back there could be a bit more text and information. But I'm open too suggestions....
I'm not too sure about the wording yet. But here are some text that I might be use:

Is sleep an issue in your home?

Is your baby having trouble sleeping? ... are you?!
I can help!

Sleep, baby, sleep….

Teaching children how to sleep

The Quiet Meadow Studio is a pediatric sleep consultancy that specializes in helping parents with children who struggle to develop good and healthy sleep habits.
Disruptive sleep patterns or not enough sleep can affect the physical, mental and emotional development of your child.

Of course nobody plans to have a sleep problem, but habits can become easily ingrained and spiral quickly out of control and you can find yourself sleep deprived, desperate and not too sure what to do. You see all the other sleeping babies and wish there was someone who understood what you were going through?! Well, there is!

Contact me for a free 15 minute consultation.

This 15 minute „mini“ consultation is a chance to discuss your unique sleep challenges and sleep goals with me. I will provide you with an overview of how I will work with your family to achieve your wildest sleep dreams (goals).
Furthermore do I understand and believe that every child and their family is unique and there is no one size fits all!
I would love to have a chat with you and talk about how I can help make things easier for you and your family!

Do I need a sleep consultant for my child?
The answer is yes if:
- if your child will only fall asleep when nursing or bottle feeding
- if your child needs a dummy or other external aid, like being rocked, patted or taken for a care ride to fall asleep
- if your good night routine is a challenging and exhausting procedure instead of a relaxed and enjoyable moment for the whole family
- if sleep is a constant battle in your home which leaves you feeling frustrated and exhausted
- if your own lack of sleep is taking a toll on you and the whole family

What can I do for you?

I will:

- Guide you to set an age appropriate foundation for good sleep
- Create an individual sleep plan tailored especially to your child’s sleep needs and circumstances
- Help you to teach your childto go to sleep and get back to sleep independently during the night
- show you how to teach your child to take healthful, restorative naps
-Learn

Contact:

Marta Lindqvist
info@quietmeadowstudio-example.com
www.quietmeadowstudio-example.com
+34 612 380 574

Consultations in English, German or Spanish via Phone/video call or home consultation

Reason: I have to go on a business trip and won't be able to choose a design until the deadline. During the trip I won't have time to give feedback and ask for changes. thank you

Target Market(s)

parents, sleep deprived mothers, young families, child care provider,

Industry/Entity Type

Baby Care

Contact Information for Business Card

Marta Lindqvist
pediatric sleep consultant
+34 612 380 574

```html
<!DOCTYPE html>
<html lang="en">
<head>
<meta charset="utf-8">
<title>The Quiet Meadow Studio – A5 Flyer Front and Back</title>
<link href="https://fonts.googleapis.com/css2?family=Ultra&family=Arimo:ital,wght@0,400;0,700;1,400&family=Raleway:wght@300&display=swap" rel="stylesheet">
<style>
  :root {
    --backdrop: #d6f6f8;
    --sky: #c2f1f6;
    --sky-deep: #a6e7ef;
    --page-edge: #5fc6cf;
    --cloud: #ffffff;
    --cloud-rim: #f3e4f1;
    --signal-red: #f0401f;
    --ink: #111111;
    --logo-ink: #8aa7a5;
    --photo-rose-a: #f7c9d6;
    --photo-rose-b: #fdf0f4;
    --photo-warm-a: #f3dccd;
    --photo-warm-b: #fbf7f4;
  }
  * { box-sizing: border-box; margin: 0; padding: 0; }
  html, body { width: 1200px; height: 1200px; overflow: hidden; }
  body {
    background: var(--backdrop);
    font-family: "Arimo", Arial, sans-serif;
    color: var(--ink);
    position: relative;
  }
  .flyer {
    position: absolute;
    top: 233px;
    width: 517px;
    height: 734px;
    background: var(--sky);
    border: 1px solid var(--page-edge);
    overflow: hidden;
  }
  .flyer--front { left: 54px; }
  .flyer--back { left: 630px; }
  .abs { position: absolute; }
  .layer { position: absolute; left: 0; top: 0; }

  .headline {
    position: absolute;
    right: 18px;
    top: 20px;
    width: 300px;
    text-align: center;
    font-family: "Ultra", Georgia, serif;
    font-size: 37px;
    line-height: 44px;
    color: var(--signal-red);
    -webkit-text-stroke: 1px #ffffff;
    text-shadow: 2px 2px 0 #ffffff, 3px 3px 0 #3a1a14;
  }
  .studio-name {
    position: absolute;
    font-family: "Raleway", Arial, sans-serif;
    font-weight: 300;
    color: var(--logo-ink);
    text-align: center;
    white-space: nowrap;
  }
  .studio-name .dot {
    display: block;
    width: 14px; height: 14px;
    border-radius: 50%;
    border: 1.5px solid #e2a7ac;
    margin: 0 auto 6px;
  }
  .intro {
    left: 9px; top: 432px; width: 292px;
    font-size: 8.6px; line-height: 12.6px; text-align: center;
  }
  .intro b { color: var(--signal-red); }
  .story {
    left: 20px; top: 494px; width: 477px;
    font-size: 7.6px; line-height: 11.2px; text-align: center; font-style: italic;
  }
  .offer {
    left: 0; width: 100%; top: 549px;
    font-size: 16.5px; text-align: center; color: var(--signal-red);
  }
  .offer-detail {
    left: 14px; top: 576px; width: 489px;
    font-size: 8.2px; line-height: 14.4px; text-align: center;
  }
  .offer-detail span { color: var(--signal-red); }
  .contact-label {
    left: 214px; top: 671px;
    font-weight: 700; font-size: 16px;
  }
  .person {
    font-family: "Ultra", Georgia, serif;
    color: var(--signal-red);
    white-space: nowrap;
  }
  .links {
    font-size: 7.6px; line-height: 11.5px; font-weight: 700; white-space: nowrap;
  }
  .phone {
    font-family: "Ultra", Georgia, serif;
    color: var(--signal-red);
    white-space: nowrap;
    -webkit-text-stroke: 0.8px #ffffff;
    text-shadow: 2px 2px 0 #3a1a14;
    letter-spacing: -0.5px;
  }
  .languages {
    left: 0; width: 100%;
    font-size: 7.6px; text-align: center; text-transform: uppercase;
  }
  .question {
    left: 12px; top: 367px; width: 210px;
    font-weight: 700; font-size: 11px; line-height: 12.5px;
    color: var(--signal-red); text-align: center;
  }
  .answer {
    left: 50px; top: 404px;
    font-weight: 700; font-size: 12.5px;
  }
  .checklist {
    list-style: none;
    font-size: 7.3px; line-height: 16px;
  }
  .checklist li::before { content: "• "; }
  .reasons { left: 5px; top: 428px; width: 510px; }
  .divider {
    left: 100px; top: 517px; width: 320px; height: 1px;
    background: linear-gradient(90deg, transparent, #ffffff, transparent);
  }
  .services-title {
    left: 8px; top: 553px; width: 100px;
    font-weight: 700; font-size: 11px; line-height: 12.5px;
    color: var(--signal-red); text-align: center;
  }
  .services { left: 119px; top: 528px; width: 395px; }
</style>
</head>
<body>

<!-- FRONT -->
<section class="flyer flyer--front">
  <svg class="layer" width="517" height="734" viewBox="0 0 517 734">
    <defs>
      <linearGradient id="rosePhoto" x1="0" y1="0" x2="1" y2="1">
        <stop offset="0" stop-color="var(--photo-rose-a)"/>
        <stop offset="0.55" stop-color="var(--photo-rose-b)"/>
        <stop offset="1" stop-color="var(--photo-rose-a)"/>
      </linearGradient>
    </defs>
    <path d="M0 170 C20 60 120 0 230 0 L517 0 L517 360 C470 330 410 360 380 410 C300 420 190 410 120 390 C60 370 20 340 0 300 Z"
          fill="url(#rosePhoto)" stroke="var(--cloud)" stroke-width="9" role="img" aria-label="Photo of a baby sleeping peacefully on a soft pink blanket"/>
    <path d="M300 400 C295 365 330 340 360 350 C370 320 410 310 435 330 C455 305 500 310 510 345 C525 360 525 400 500 420 C495 450 460 460 440 450 C420 470 380 470 365 455 C335 465 300 450 305 425 Z"
          fill="var(--cloud)" stroke="var(--cloud-rim)" stroke-width="3"/>
    <path d="M0 690 C15 665 45 655 70 668 C90 645 130 645 150 665 C170 650 200 655 210 670 L220 670 C225 625 270 610 300 630 C330 615 370 625 380 650 C410 640 450 645 470 665 C490 660 510 670 517 680 L517 734 L0 734 Z"
          fill="var(--cloud)"/>
  </svg>

  <h1 class="headline">Sleep, Baby,<br>Sleep....</h1>

  <div class="studio-name" style="left:296px; top:367px; width:210px; font-size:15px;">
    <span class="dot"></span>The Quiet Meadow Studio
  </div>

  <p class="abs intro">The <b>Quiet Meadow Studio</b> is a pediatric sleep consultancy that specializes in helping parents with children who struggle to develop good and healthy sleep habits. Disruptive sleep patterns or not enough sleep can affect the physical, mental and emotional development of your child.</p>

  <p class="abs story">Of course nobody plans to have a sleep problem, but habits can become easily ingrained and spiral quickly out of control and you can find yourself sleep deprived, desperate and not too sure what to do. You see all the other sleeping babies and wish there was someone who understood what you were going through?! Well, there is!</p>

  <h2 class="abs offer">CONTACT ME FOR A FREE 15 MINUTE CONSULTATION.</h2>

  <p class="abs offer-detail">This <span>15 minutes</span> "mini" consultation is a chance to discuss your unique sleep challenges and sleep goals with me.<br>I will provide you with an overview of how I will work with your family to achieve your wildest sleep dreams (goals).<br>Furthermore do I understand and believe that every child and their family is unique and there is no one size fits all!<br>I would love to have a chat with you and talk about how I can help make things easier for you and your family!</p>

  <p class="abs contact-label">CONTACT:</p>
  <p class="abs person" style="left:6px; top:693px; font-size:16px;">Marta Lindqvist</p>
  <p class="abs links" style="left:141px; top:691px;">info@quietmeadowstudio-example.com<br>www.quietmeadowstudio-example.com</p>
  <p class="abs phone" style="left:298px; top:686px; font-size:21px;">+34 612 380 574</p>
  <p class="abs languages" style="top:720px;">Consultations in English, German or Spanish via phone/video call or home consultation</p>
</section>

<!-- BACK -->
<section class="flyer flyer--back">
  <svg class="layer" width="517" height="734" viewBox="0 0 517 734">
    <defs>
      <linearGradient id="warmPhoto" x1="0" y1="0" x2="1" y2="0.6">
        <stop offset="0" stop-color="var(--photo-warm-a)"/>
        <stop offset="0.5" stop-color="var(--photo-warm-b)"/>
        <stop offset="1" stop-color="var(--photo-warm-a)"/>
      </linearGradient>
    </defs>
    <path d="M0 0 L517 0 L517 395 L0 395 Z" fill="url(#warmPhoto)" role="img" aria-label="Photo of a mother resting beside her sleeping baby in white bedding"/>
    <path d="M0 350 C60 340 130 340 200 355 C240 365 250 385 260 395 L0 395 Z" fill="var(--sky)"/>
    <path d="M240 330 C230 295 270 270 300 285 C315 250 360 245 385 265 C410 240 465 250 470 280 C500 280 525 310 510 345 C520 375 490 405 460 400 C440 425 400 425 385 410 C360 425 320 420 315 400 C280 410 245 390 255 365 C235 360 230 340 240 330 Z"
          fill="var(--cloud)" stroke="var(--cloud-rim)" stroke-width="3"/>
    <path d="M0 610 C30 590 60 595 80 610 C110 585 150 585 175 605 C200 590 240 590 260 610 C285 590 330 590 350 608 C380 590 420 590 440 608 C470 592 505 598 517 612 L517 734 L0 734 Z"
          fill="var(--sky-deep)"/>
    <path d="M0 650 C30 630 70 635 90 650 C120 628 160 630 180 648 C210 630 250 632 270 650 C300 632 340 632 360 650 C390 632 430 634 450 650 C475 635 505 640 517 652 L517 734 L0 734 Z"
          fill="var(--cloud)"/>
  </svg>

  <div class="studio-name" style="left:236px; top:300px; width:280px; font-size:18px;">
    <span class="dot"></span>The Quiet Meadow Studio
  </div>

  <h2 class="abs question">DO I NEED A SLEEP<br>CONSULTANT FOR MY CHILD?</h2>
  <p class="abs answer">The Answer Is Yes If:</p>

  <ul class="abs checklist reasons">
    <li>If your child will only fall asleep when nursing or bottle feeding</li>
    <li>If your child needs a dummy or other external aid, like being rocked, patted or taken for a care ride to fall asleep</li>
    <li>If your good night routine is a challenging and exhausting procedure instead of a relaxed and enjoyable moment for the whole family</li>
    <li>If sleep is a constant battle in your home which leaves you feeling frustrated and exhausted</li>
    <li>If your own lack of sleep is taking a toll on you and the whole family</li>
  </ul>

  <div class="abs divider"></div>

  <h2 class="abs services-title">WHAT CAN I<br>DO FOR YOU?</h2>
  <ul class="abs checklist services">
    <li>Guide you to set an age appropriate foundation for good sleep</li>
    <li>Create an individual sleep plan tailored especially to your child's sleep needs and circumstances</li>
    <li>Help you to teach your childto go to sleep and get back to sleep independently during the night</li>
    <li>Show you how to teach your child to take healthful, restorative naps</li>
    <li>Learn</li>
  </ul>

  <p class="abs person" style="left:32px; top:667px; font-size:16px; text-transform:uppercase;">Marta Lindqvist</p>
  <p class="abs links" style="left:40px; top:686px;">info@quietmeadowstudio-example.com<br>www.quietmeadowstudio-example.com</p>
  <p class="abs phone" style="left:210px; top:674px; font-size:28px;">+34 612 380 574</p>
  <p class="abs languages" style="top:716px;">Consultations in English, German or Spanish via phone/video call or home consultation</p>
</section>

</body>
</html>
```